Company Banner

I would like our 5 corporate Core Values placed on a single banner that has a theme related to our engineering industry.

Core Values: Productive & Hard Working, Professional, Humble, Personable, Adaptable

Target Market(s)

Construction, Engineering

Requirements
Must have
• All words randomly positioned on the banner with color and industry background images.

Please add company logo to upper left corner as well (attached logo design file)

```html
<!DOCTYPE html>
<html lang="en">
<head>
<meta charset="utf-8">
<title>Core Values Banner</title>
<link rel="stylesheet" href="https://fonts.googleapis.com/css2?family=Anton&display=swap">
<style>
  :root {
    --page-bg: #ffffff;
    --value-blue: #1f6ef2;
    --value-orange: #ff8a12;
    --value-outline: #ffffff;
    --plate-fill: rgba(12, 18, 32, 0.72);
    --plate-edge: rgba(220, 228, 240, 0.85);
    --swoosh-orange: #ff8c0a;
    --swoosh-blue: #2a8cf5;
  }
  html, body {
    margin: 0;
    padding: 0;
    width: 1200px;
    height: 1200px;
    overflow: hidden;
    background: var(--page-bg);
  }
  .canvas {
    position: relative;
    width: 1200px;
    height: 1200px;
  }
  .core-values-banner {
    position: absolute;
    left: 87px;
    top: 330px;
    width: 1025px;
    height: 576px;
    display: block;
  }
  .value-plate {
    fill: var(--plate-fill);
    stroke: var(--plate-edge);
    stroke-width: 2;
  }
  .value-word {
    font-family: "Anton", "Oswald", sans-serif;
    font-size: 72px;
    text-anchor: middle;
    paint-order: stroke fill;
    stroke: var(--value-outline);
    stroke-width: 4px;
    stroke-linejoin: round;
  }
  .value-word--blue { fill: var(--value-blue); }
  .value-word--orange { fill: var(--value-orange); }
</style>
</head>
<body>
<main class="canvas">
  <svg class="core-values-banner" viewBox="0 0 1281 720" preserveAspectRatio="none" aria-label="Core values banner">
    <defs>
      <linearGradient id="plant-photo-tones" x1="0" y1="0" x2="1" y2="1">
        <stop offset="0" stop-color="#f2a93a"/>
        <stop offset="0.3" stop-color="#9a6a3c"/>
        <stop offset="0.55" stop-color="#4a5a6e"/>
        <stop offset="0.8" stop-color="#2c3a4c"/>
        <stop offset="1" stop-color="#b87a34"/>
      </linearGradient>
      <radialGradient id="welding-photo-tones" cx="0.82" cy="0.72" r="0.6">
        <stop offset="0" stop-color="#f6e2a0"/>
        <stop offset="0.25" stop-color="#8a7a52"/>
        <stop offset="0.6" stop-color="#2a4058"/>
        <stop offset="1" stop-color="#162434"/>
      </radialGradient>
      <linearGradient id="blue-sweep" x1="0" y1="0" x2="1" y2="0">
        <stop offset="0.35" stop-color="var(--swoosh-blue)" stop-opacity="1"/>
        <stop offset="0.75" stop-color="var(--swoosh-blue)" stop-opacity="0.15"/>
        <stop offset="1" stop-color="var(--swoosh-blue)" stop-opacity="0"/>
      </linearGradient>
    </defs>

    <rect class="plant-photo" x="0" y="0" width="1281" height="720" fill="url(#plant-photo-tones)"
          role="img" aria-label="Photo of an industrial plant with steel pipes, pressure gauges and valves"/>

    <path class="welding-photo" d="M400,720 C640,600 860,330 1005,0 L1281,0 L1281,720 Z" fill="url(#welding-photo-tones)"
          role="img" aria-label="Photo of a factory welding robot throwing bright sparks"/>

    <path class="swoosh swoosh--orange" d="M260,720 C520,560 780,330 905,0 L1005,0 C860,330 640,600 400,720 Z" fill="var(--swoosh-orange)"/>
    <path class="swoosh swoosh--blue" d="M400,720 C640,600 860,330 1005,0 L1281,0 L1281,720 Z" fill="url(#blue-sweep)"/>

    <g class="value value--professional">
      <rect class="value-plate" x="84" y="107" width="399" height="107"/>
      <text class="value-word value-word--blue" x="283" y="188" textLength="272" lengthAdjust="spacingAndGlyphs">Professional</text>
    </g>

    <g class="value value--humble">
      <rect class="value-plate" x="425" y="257" width="264" height="108"/>
      <text class="value-word value-word--blue" x="555" y="338" textLength="160" lengthAdjust="spacingAndGlyphs">Humble</text>
    </g>

    <g class="value value--productive">
      <rect class="value-plate" x="793" y="62" width="398" height="197"/>
      <text class="value-word value-word--orange" x="991" y="144" textLength="231" lengthAdjust="spacingAndGlyphs">Productive</text>
      <text class="value-word value-word--orange" x="991" y="226" textLength="335" lengthAdjust="spacingAndGlyphs">&amp; Hard Working</text>
    </g>

    <g class="value value--personable">
      <rect class="value-plate" x="578" y="428" width="345" height="107"/>
      <text class="value-word value-word--orange" x="750" y="507" textLength="242" lengthAdjust="spacingAndGlyphs">Personable</text>
    </g>

    <g class="value value--adaptable">
      <rect class="value-plate" x="166" y="530" width="304" height="108"/>
      <text class="value-word value-word--blue" x="318" y="612" textLength="210" lengthAdjust="spacingAndGlyphs">Adaptable</text>
    </g>
  </svg>
</main>
</body>
</html>
```